Verlin Auto Repair - Flyer Design

My business is a automobile shop where we fix cars. Such things that we do but not limited to is brakes, Engine/Transmission change, Electrical work, emission test, oil change and automobile diagnostic. I am looking for a flyer that will catch peoples attention, I will be giving flyers to people, putting them in car windows and mailboxes. I am looking for a flier that will help to attract more customers to my business. I also want the flyer to say "Bring in your estimate from our competitors with this flyer and we will beat it by 10%" (does not have to be in those exact words). I also want the flyer to have my business address phone and operating hours. I have attached a business card and my business ad which I have placed in the newspaper before. I hope it helps with your design.
Industry/Entity Type
Car Repair
Look and feel
Each slider illustrates characteristics of the customer's brand and the style your logo design should communicate.

```html
<!DOCTYPE html>
<html lang="en">
<head>
<meta charset="utf-8">
<title>Verlin Auto Repair – Flyer</title>
<link rel="stylesheet" href="https://fonts.googleapis.com/css2?family=Dosis:wght@500;600&family=Lato:wght@400;700;900&family=Ubuntu:wght@500;700&display=swap">
<style>
  :root {
    --ink-dark: #1c1c1c;
    --band-dark: #2b2b2b;
    --orange: #f7931e;
    --orange-deep: #f26a10;
    --red: #c4242f;
    --blue: #3f69b2;
    --grey-text: #7a7a7a;
    --panel: #f6ead2;
    --panel-line: #e2d3b6;
    --panel-title: #5c5a55;
    --white: #ffffff;
    --bg-center: #ffffff;
    --bg-edge: #dfe0e3;
  }
  html, body {
    margin: 0;
    padding: 0;
    width: 1200px;
    height: 800px;
    overflow: hidden;
  }
  .flyer {
    position: relative;
    width: 1200px;
    height: 800px;
    overflow: hidden;
    background: radial-gradient(ellipse 70% 60% at 40% 55%, var(--bg-center) 0%, #f3f4f6 55%, var(--bg-edge) 100%);
    font-family: "Lato", sans-serif;
  }
  .top-band {
    position: absolute;
    inset: 0 0 auto 0;
    height: 40px;
    background: linear-gradient(180deg, #3a3a3a, var(--band-dark));
  }
  .top-stripe {
    position: absolute;
    left: 580px;
    top: 40px;
    width: 620px;
    height: 11px;
    background: var(--orange);
  }
  .brand-banner {
    position: absolute;
    left: 0;
    top: 0;
    width: 640px;
    height: 190px;
  }
  .brand-name {
    position: absolute;
    left: 95px;
    top: 44px;
    margin: 0;
    font-family: "Ubuntu", sans-serif;
    font-weight: 700;
    font-size: 46px;
    letter-spacing: -1.5px;
    color: var(--ink-dark);
    line-height: 1;
  }
  .brand-tagline {
    position: absolute;
    left: 100px;
    top: 100px;
    margin: 0;
    font-family: "Ubuntu", sans-serif;
    font-weight: 500;
    font-size: 19px;
    color: var(--white);
  }
  .headline {
    position: absolute;
    left: 46px;
    top: 222px;
    margin: 0;
    font-family: "Ubuntu", sans-serif;
    font-weight: 500;
    line-height: 1;
  }
  .headline-lead {
    display: block;
    font-size: 66px;
    color: var(--red);
    letter-spacing: -0.5px;
  }
  .headline-main {
    display: block;
    margin-top: 8px;
    font-size: 93px;
    color: var(--blue);
    letter-spacing: -1px;
  }
  .promise {
    position: absolute;
    left: 50px;
    top: 388px;
    margin: 0;
    font-weight: 700;
    font-size: 36px;
    line-height: 1.1;
    color: var(--grey-text);
  }
  .offer {
    position: absolute;
    left: 50px;
    top: 438px;
    margin: 0;
    font-weight: 900;
    font-size: 22px;
    line-height: 1.2;
    color: var(--red);
  }
  .offer-highlight { color: var(--orange-deep); }
  .services {
    position: absolute;
    left: 50px;
    top: 484px;
    margin: 0;
    padding: 0;
    list-style: none;
    font-size: 17px;
    font-weight: 700;
    line-height: 23px;
    color: var(--ink-dark);
  }
  .service {
    position: relative;
    padding-left: 18px;
  }
  .service::before {
    content: "";
    position: absolute;
    left: 0;
    top: 8px;
    width: 8px;
    height: 8px;
    background: var(--orange);
  }
  .hours-panel {
    position: absolute;
    left: 917px;
    top: 57px;
    width: 221px;
    height: 386px;
  }
  .hours-panel svg { position: absolute; inset: 0; }
  .hours-content {
    position: absolute;
    inset: 0;
    text-align: center;
    font-family: "Dosis", sans-serif;
  }
  .hours-title {
    margin: 20px 0 0;
    color: var(--panel-title);
    font-weight: 500;
    line-height: 1;
  }
  .hours-title .small { display: block; font-size: 31px; }
  .hours-title .large { display: block; font-size: 43px; margin-top: 2px; }
  .hours-list { list-style: none; margin: 15px 0 0; padding: 0; }
  .hours-item {
    border-top: 1px solid var(--panel-line);
    margin: 0 10px;
    padding: 8px 0 0;
    height: 78px;
    box-sizing: border-box;
    font-family: "Lato", sans-serif;
  }
  .hours-day { display: block; font-size: 21px; font-family: "Dosis", sans-serif; font-weight: 600; }
  .hours-day.weekday { color: var(--blue); }
  .hours-day.weekend { color: var(--red); }
  .hours-time { display: block; font-size: 20px; font-weight: 700; color: var(--ink-dark); margin-top: 4px; }
  .vehicles {
    position: absolute;
    left: 412px;
    top: 478px;
    width: 780px;
    height: 225px;
    border-radius: 40% 40% 12px 12px / 35% 35% 12px 12px;
    background: linear-gradient(90deg, #4a69c4 0%, #3a58b0 45%, #1e1f24 60%, #121316 100%);
    opacity: 0.9;
  }
  .office {
    position: absolute;
    left: 49px;
    top: 600px;
    margin: 0;
    font-style: normal;
    font-size: 25px;
    line-height: 1.3;
    color: var(--ink-dark);
  }
  .office-label { display: block; font-weight: 700; }
  .contact-bar {
    position: absolute;
    left: 0;
    bottom: 0;
    width: 1200px;
    height: 78px;
    background: #141414;
    color: var(--white);
    font-weight: 700;
    font-size: 28px;
  }
  .contact-email { position: absolute; left: 122px; top: 21px; }
  .contact-phone { position: absolute; left: 697px; top: 21px; }
</style>
</head>
<body>
<div class="flyer">
  <div class="top-band"></div>
  <div class="top-stripe"></div>

  <header class="brand">
    <svg class="brand-banner" viewBox="0 0 640 190" aria-hidden="true">
      <defs>
        <linearGradient id="bannerFill" x1="0" y1="0" x2="0" y2="1">
          <stop offset="0" stop-color="#fbab2a"/>
          <stop offset="1" stop-color="#f26410"/>
        </linearGradient>
      </defs>
      <polygon points="0,40 40,40 40,52" fill="#b3520c"/>
      <polygon points="40,9 594,9 628,48 628,132 334,184 40,132" fill="url(#bannerFill)"/>
    </svg>
    <h1 class="brand-name">VerlinAutoRepair</h1>
    <p class="brand-tagline">Specializing in Foreign &amp; Domestic cars</p>
  </header>

  <h2 class="headline">
    <span class="headline-lead">Bring Back That</span>
    <span class="headline-main">NEW CAR FEELING</span>
  </h2>
  <p class="promise">We Get the job Done right the First Time!</p>
  <p class="offer">Bring a competitor's estimate with this flyer &ndash; we'll <span class="offer-highlight">beat it by 10%!</span></p>

  <ul class="services">
    <li class="service">Brakes &middot; Oil Change</li>
    <li class="service">Engine &amp; Transmission</li>
    <li class="service">Electrical Work &middot; Emission Test</li>
    <li class="service">Computer Diagnostics</li>
  </ul>

  <aside class="hours-panel">
    <svg viewBox="0 0 221 386" width="221" height="386" aria-hidden="true">
      <polygon points="0,0 221,0 221,386 110.5,354 0,386" fill="var(--panel)"/>
    </svg>
    <div class="hours-content">
      <h3 class="hours-title"><span class="small">Hours of</span><span class="large">Operation</span></h3>
      <ul class="hours-list">
        <li class="hours-item"><span class="hours-day weekday">Monday to Friday</span><span class="hours-time">8am - 5pm</span></li>
        <li class="hours-item"><span class="hours-day weekend">SATURDAY</span><span class="hours-time">8am - 1pm</span></li>
        <li class="hours-item"><span class="hours-day weekend">SUNDAY</span><span class="hours-time">Closed</span></li>
      </ul>
    </div>
  </aside>

  <div class="vehicles" role="img" aria-label="Photo of a blue convertible and a black SUV parked side by side"></div>

  <address class="office">
    <span class="office-label">Our Office</span>
    4127 S. Harbor Ave.<br>
    Chicago IL. 60619
  </address>

  <footer class="contact-bar">
    <span class="contact-email">Email: VerlinAutoRepair@mailhub.net</span>
    <span class="contact-phone">Call Now: (773) 555-0148</span>
  </footer>
</div>
</body>
</html>
```